Business Card Design

I am specialising in Designs, Drafting and Council approvals. From the idea to the full set of plans and other documents. Residential houses only.
I am located in Northern Beaches, Sydney where the sky is always blue :)
Tallwood Drafting should be associated with light, modern house designs & with 3D drafting. I am positive person, that would like help every client through the demanding time of council paperwork.

The business card should be light blue, with white 3D sketch and white or black writing. Simple, modern and "happy"

Please don't hesitate to suggest something if you think so.

Thanks
Mirela

Industry/Entity Type

House

Contact Information for Business Card

FRONT:

Tallwood Drafting
Servicing Northern Beaches

Mirela Ostrowe
tallwooddrafting@mailhaven.com.au
0427 586 293
www.tallwooddrafting.com.au

BACK:

Design consultation
Plans Drafting
3D Visualisation
Council Approvals

```html
<!DOCTYPE html>
<html lang="en">
<head>
<meta charset="utf-8">
<title>Tallwood Drafting – Business Card</title>
<link href="https://fonts.googleapis.com/css2?family=Lexend:wght@400;600&family=Questrial&display=swap" rel="stylesheet">
<style>
  :root {
    --stage: #3b3440;
    --sky-deep: #1489c4;
    --sky-panel: #27a6e0;
    --sky-light: #1fb8ec;
    --sky-strip: #1596cf;
    --ink-line: rgba(20, 70, 110, 0.55);
    --white: #ffffff;
  }
  * { box-sizing: border-box; margin: 0; padding: 0; }
  html, body { width: 1200px; height: 800px; overflow: hidden; }
  body {
    background: var(--stage);
    font-family: "Questrial", sans-serif;
    color: var(--white);
    position: relative;
  }
  .card {
    position: absolute;
    top: 257px;
    width: 500px;
    height: 286px;
    overflow: hidden;
    box-shadow: 0 12px 30px rgba(0,0,0,0.35);
  }

  /* ---------- Back card ---------- */
  .card--back { left: 70px; background: var(--sky-light); }
  .floor-plan {
    position: absolute; left: 22px; top: 22px; width: 230px; height: 218px;
    background: linear-gradient(135deg, #2cbdee, #18a6dc);
    border: 1px solid var(--ink-line);
  }
  .back-title {
    position: absolute; right: 24px; top: 30px;
    font-family: "Lexend", sans-serif; font-weight: 400;
    font-size: 23px; letter-spacing: 1.5px; text-transform: uppercase;
    white-space: nowrap;
    padding-bottom: 8px; border-bottom: 1px solid rgba(255,255,255,0.7);
  }
  .services {
    position: absolute; right: 30px; top: 150px; list-style: none;
    font-size: 15px; font-variant: small-caps; letter-spacing: 1px; line-height: 1.55;
  }
  .services li { display: flex; align-items: center; gap: 10px; white-space: nowrap; }
  .services svg { width: 8px; height: 9px; flex: none; }
  .web-strip {
    position: absolute; left: 0; bottom: 0; width: 100%; height: 28px;
    background: var(--sky-strip);
    display: flex; align-items: center; padding-left: 22px;
    font-size: 10px; letter-spacing: 4.5px; text-transform: uppercase;
  }

  /* ---------- Front card ---------- */
  .card--front { left: 630px; background: var(--sky-deep); }
  .contact-panel {
    position: absolute; left: 16px; top: 0; width: 240px; height: 236px;
    background: var(--sky-panel);
    padding: 18px 12px 0 20px;
  }
  .contact-panel::after {
    content: ""; position: absolute; right: -18px; top: 42px;
    border-left: 18px solid var(--sky-panel);
    border-top: 14px solid transparent; border-bottom: 14px solid transparent;
  }
  .person-name { font-size: 15px; letter-spacing: 1px; text-transform: uppercase; white-space: nowrap; }
  .person-role { font-size: 10px; letter-spacing: 1px; margin-top: 2px; }
  .location { text-align: center; margin-top: 14px; font-size: 11px; letter-spacing: 1px; text-transform: uppercase; line-height: 1.35; }
  .location svg { display: block; margin: 0 auto 6px; width: 18px; height: 22px; }
  .contacts { list-style: none; margin-top: 12px; font-size: 8px; letter-spacing: 0.3px; text-transform: uppercase; }
  .contacts li { display: flex; align-items: center; gap: 7px; height: 20px; white-space: nowrap; }
  .contacts svg { width: 13px; height: 13px; flex: none; }
  .front-title {
    position: absolute; right: 18px; top: 46px; text-align: right;
    font-family: "Lexend", sans-serif; font-weight: 600;
    font-size: 15px; letter-spacing: 0.6px; line-height: 1.25; text-transform: uppercase;
    white-space: nowrap;
  }
  .house-sketch {
    position: absolute; right: 24px; bottom: 22px; width: 200px; height: 132px;
    background: linear-gradient(160deg, #1b95cf, #117cb5);
    border: 1px solid rgba(10,50,90,0.35);
  }
</style>
</head>
<body>

  <section class="card card--back" aria-label="Card back">
    <div class="floor-plan" role="img" aria-label="Line drawing of a house floor plan"></div>
    <h2 class="back-title">Tallwood Drafting</h2>
    <ul class="services">
      <li><svg viewBox="0 0 8 9"><path d="M0 0 L8 4.5 L0 9 Z" fill="#ffffff"/></svg>Design Consultation</li>
      <li><svg viewBox="0 0 8 9"><path d="M0 0 L8 4.5 L0 9 Z" fill="#ffffff"/></svg>Plans Drafting</li>
      <li><svg viewBox="0 0 8 9"><path d="M0 0 L8 4.5 L0 9 Z" fill="#ffffff"/></svg>3D Visualisation</li>
      <li><svg viewBox="0 0 8 9"><path d="M0 0 L8 4.5 L0 9 Z" fill="#ffffff"/></svg>Council Approvals</li>
    </ul>
    <div class="web-strip">www.tallwooddrafting.com.au</div>
  </section>

  <section class="card card--front" aria-label="Card front">
    <div class="contact-panel">
      <p class="person-name">Mirela Ostrowe</p>
      <p class="person-role">Director</p>
      <div class="location">
        <svg viewBox="0 0 18 22"><circle cx="9" cy="11" r="8" fill="none" stroke="#fff" stroke-width="1.2"/><path d="M9 5.5a3.2 3.2 0 0 0-3.2 3.2C5.8 11.2 9 15.5 9 15.5s3.2-4.3 3.2-6.8A3.2 3.2 0 0 0 9 5.5z" fill="none" stroke="#fff" stroke-width="1.1"/><circle cx="9" cy="8.7" r="1.1" fill="#fff"/></svg>
        Northern Beaches<br>Sydney
      </div>
      <ul class="contacts">
        <li><svg viewBox="0 0 13 13"><circle cx="6.5" cy="6.5" r="6" fill="none" stroke="#fff" stroke-width="0.9"/><rect x="3.5" y="4.5" width="6" height="4" fill="none" stroke="#fff" stroke-width="0.8"/><path d="M3.5 4.5 L6.5 7 L9.5 4.5" fill="none" stroke="#fff" stroke-width="0.8"/></svg>tallwooddrafting@mailhaven.com.au</li>
        <li><svg viewBox="0 0 13 13"><circle cx="6.5" cy="6.5" r="6" fill="none" stroke="#fff" stroke-width="0.9"/><circle cx="6.5" cy="6.5" r="3.2" fill="none" stroke="#fff" stroke-width="0.8"/><path d="M3.3 6.5h6.4M6.5 3.3c-1.4 2-1.4 4.4 0 6.4M6.5 3.3c1.4 2 1.4 4.4 0 6.4" fill="none" stroke="#fff" stroke-width="0.6"/></svg>www.tallwooddrafting.com.au</li>
        <li><svg viewBox="0 0 13 13"><circle cx="6.5" cy="6.5" r="6" fill="none" stroke="#fff" stroke-width="0.9"/><rect x="4.8" y="3.3" width="3.4" height="6.4" rx="0.6" fill="none" stroke="#fff" stroke-width="0.8"/></svg>0427 586 293</li>
      </ul>
    </div>
    <h1 class="front-title">Tallwood Drafting<br>Servicing</h1>
    <div class="house-sketch" role="img" aria-label="Line sketch of a two-storey residential house in perspective"></div>
  </section>

</body>
</html>
```